Christmas social media advert post

I am looking for an eye catching advert for use mainly on social media posts.
The following is the detail of the event.

Christmas special offer-
£10pp,– offer includes –
Half an hour Toboggan track,
Half an hour Slingshot paintballs (20 paintballs pp) and safe target archery (under cover and indoor ranges). Activities all the family from age 4 to grandparents can join in,
Also available – Add on indoor activities including Mini Curling, Bead Blitz, Safe axe throwing, Air juggler – from £3.50pp and age 6plus
Café open for hot food and drinks in the ‘Fireside Frost Lodge and the heated Christmas marquee.

A basic idea I put together for what I feel is the important information is -

Christmas Special offer -
Starts Saturday 20th December.
£10pp – offer includes –
Half an hour Slingshot paintballs (20 paintballs pp) and safe target archery (under cover and indoor ranges). Activities all the family from age 4 to grandparents can join in. Booking is essential - details on how below.
Also available Add on indoor activities - including Mini Curling, Bead Blitz, Safe axe throwing, Air juggler – from £3.50pp and age 6plus.
Ages start from 4 plus.
All activities are great for children and adults so perfect for families as well as friends, parties and get togethers.
Free huge car parks,
Booking is easy-
Just Message from messenger (on this post) or email
martin@hollowbrookleisurepark.co.uk for availability of your preferred date and time.

I would be happy to send the detailed information to enquiries if it meant a better looking advert / post.

Full details are in the picture uploads, feel free to use as much or as little of the information as you feel best.

```html
<!DOCTYPE html>
<html lang="en">
<head>
<meta charset="utf-8">
<title>Christmas Special Offer – Hollowbrook Leisure Park</title>
<link href="https://fonts.googleapis.com/css2?family=Oswald:wght@500;600;700&family=Poppins:ital,wght@0,500;0,600;0,700;1,500;1,800&display=swap" rel="stylesheet">
<style>
:root{
  --red:#ee1c1c;
  --red-deep:#d9101a;
  --green:#12a43a;
  --navy:#1a2f8c;
  --yellow:#ffe600;
  --gold:#f4c21a;
  --white:#ffffff;
  --dark:#1f2326;
  --backdrop:#ede8d8;
  --pink:#f6a9ad;
}
*{margin:0;padding:0;box-sizing:border-box}
html,body{width:1200px;height:1200px;overflow:hidden;background:var(--backdrop)}
.flyer{position:absolute;left:120px;top:0;width:960px;height:1200px;background:var(--red);overflow:hidden;font-family:"Poppins",sans-serif}
.abs{position:absolute}
.photo{position:absolute;overflow:hidden}
.photo-toboggan{left:0;top:0;width:585px;height:365px;background:linear-gradient(160deg,#d9d4cb 0%,#b9a994 45%,#8c3a35 80%,#c9443f 100%)}
.photo-archery{left:0;top:365px;width:621px;height:220px;background:linear-gradient(180deg,#c4c0b8 0%,#a88f74 55%,#8f8c87 100%)}
.photo-curling{left:389px;top:587px;width:500px;height:259px;border:4px solid var(--white);border-radius:10px 0 0 0;background:linear-gradient(170deg,#b9bcb5 0%,#c7a985 45%,#d8c2a4 100%)}
.photo-gel{left:0;top:692px;width:433px;height:249px;border:4px solid var(--white);border-left:none;border-radius:0 12px 12px 0;background:radial-gradient(ellipse at 55% 40%,#5a4b7a 0%,#3c3f3a 45%,#2a2c28 100%)}
.photo-cafe{left:23px;top:572px;width:165px;height:120px;border:4px solid var(--white);border-radius:10px 0 0 0;background:linear-gradient(180deg,#3a3430 0%,#7a5c44 55%,#c9b9a4 100%)}
.photo-axe{left:537px;top:850px;width:0;height:0}
.axe-target{left:540px;top:698px;width:113px;height:100px;border:5px solid var(--white);background:linear-gradient(180deg,#2a4fb0,#c9d3e6)}

.offer-col{left:585px;top:0;width:375px;height:700px;background:var(--red)}
.offer-panel{left:585px;top:0;width:343px;height:557px;background:var(--white);border-radius:0 0 24px 24px}
.title{left:585px;width:343px;text-align:center;font-family:"Oswald",sans-serif;font-weight:600;color:var(--red);line-height:1;letter-spacing:-1px}
.title-1{top:22px;font-size:74px}
.title-2{top:98px;font-size:58px}
.date-band{left:567px;top:163px;width:380px;height:74px;background:var(--green);color:var(--white);text-align:center;font-family:"Oswald",sans-serif;font-weight:500}
.date-band .starts{font-size:21px;line-height:1;padding-top:7px}
.date-band .date{font-size:33px;line-height:1.15}
.price{left:585px;top:246px;width:343px;text-align:center;color:var(--red);font-family:"Oswald",sans-serif;font-weight:700;line-height:1}
.price .amount{font-size:100px;letter-spacing:-2px}
.price .pp{font-size:50px}
.includes{left:585px;top:350px;width:343px;text-align:center;line-height:1.15}
.includes .label{color:var(--navy);font-weight:500;font-size:18px;margin-bottom:10px}
.includes .lead{color:var(--navy);font-weight:500;font-size:16px}
.includes .item{color:var(--red);font-weight:600;font-size:22px;margin-bottom:5px}
.includes .note{color:var(--navy);font-style:italic;font-weight:500;font-size:12.5px;margin:-4px 0 5px}

.miss-tag{left:341px;top:347px;width:260px;height:43px}
.miss-tag span{position:absolute;left:14px;top:2px;font-family:"Poppins",sans-serif;font-style:italic;font-weight:800;font-size:27px;color:var(--white);letter-spacing:-1px}

.cafe-strip{left:0;top:627px;width:389px;height:65px;background:var(--red)}
.cafe-card{left:184px;top:545px;width:189px;height:147px;background:var(--white);border-radius:10px 10px 0 0;text-align:center;line-height:1.1}
.cafe-card .head{color:var(--green);font-weight:600;font-size:23px;padding-top:6px}
.cafe-card .cond{font-family:"Oswald",sans-serif;font-weight:500;color:var(--red);font-size:15px;margin-top:4px}
.cafe-card .ital{font-style:italic;font-weight:500;color:var(--red);font-size:11.5px}
.cafe-card .big{font-family:"Oswald",sans-serif;font-weight:500;color:var(--red);font-size:17px}

.ages-panel{left:824px;top:587px;width:136px;height:259px;background:linear-gradient(160deg,#2e3130,#16191a);color:var(--white);text-align:right;padding:10px 10px 0 0}
.ages-panel .big{font-family:"Oswald",sans-serif;font-weight:600;font-size:28px;line-height:1}
.ages-panel .rule{height:4px;background:var(--green);margin:6px 0 8px 8px}
.ages-panel .sm{font-family:"Oswald",sans-serif;font-weight:500;font-size:13px;line-height:1.25}
.ages-panel .xs{font-family:"Oswald",sans-serif;font-weight:500;font-size:8.5px;line-height:1.3}
.ages-panel .gold{color:var(--gold)}
.ages-panel .fam{font-family:"Oswald",sans-serif;font-weight:600;font-size:22px;color:var(--gold);line-height:1}

.also-tag{left:675px;top:833px;width:140px;height:32px;background:var(--yellow);color:var(--navy);font-family:"Oswald",sans-serif;font-weight:500;font-size:21px;text-align:center;line-height:32px}
.addon{left:385px;top:866px;width:575px;text-align:center;color:var(--white);font-family:"Oswald",sans-serif;font-weight:500;line-height:1}
.addon .head{font-size:46px;font-weight:600}
.addon .head small{font-size:26px;font-weight:500}
.addon .list{font-size:18px;margin-top:10px}
.addon .price-line{font-size:18px;margin-top:10px}
.addon .y{color:var(--yellow)}
.addon .y small{font-size:12px}

.wave{left:0;top:960px;width:960px;height:240px}
.brand{left:34px;top:1000px;width:390px;height:170px;display:flex;align-items:center;gap:16px}
.brand-dot{width:120px;height:120px;border-radius:50%;background:var(--navy);flex:none}
.brand-name{font-family:"Poppins",sans-serif;font-weight:700;color:var(--white);font-size:34px;line-height:1.05}

.booking{left:455px;top:988px;width:505px;height:144px;background:var(--white);clip-path:polygon(0 0,100% 0,100% 100%,0 100%);text-align:center}
.booking .head{font-style:italic;font-weight:800;color:var(--navy);font-size:30px;line-height:1;padding-top:8px;letter-spacing:1px}
.booking .sub{color:var(--navy);font-weight:500;font-size:12.5px;margin-top:4px}
.email-band{left:455px;top:1050px;width:505px;height:41px;background:var(--green);color:var(--white);font-family:"Oswald",sans-serif;font-weight:500;font-size:19px;text-align:center;line-height:41px;letter-spacing:.3px}
.avail{left:455px;top:1102px;width:480px;text-align:center;font-style:italic;font-weight:500;color:var(--navy);font-size:14px}
.cursor{left:907px;top:1088px;width:32px;height:34px}
.parking{left:455px;top:1140px;width:480px;text-align:center;font-style:italic;font-weight:800;color:var(--white);font-size:29px;letter-spacing:2px}
</style>
</head>
<body>
<main class="flyer">
  <div class="photo photo-toboggan" role="img" aria-label="Three smiling children in helmets riding red toboggans down a wooden track"></div>
  <div class="photo photo-archery" role="img" aria-label="Two people aiming bows at round targets in a covered wooden archery range"></div>

  <div class="abs offer-col"></div>
  <div class="abs offer-panel"></div>
  <h1 class="abs title title-1">CHRISTMAS</h1>
  <h2 class="abs title title-2">SPECIAL OFFER</h2>
  <div class="abs date-band">
    <div class="starts">STARTS</div>
    <div class="date">SATURDAY 20TH DECEMBER</div>
  </div>
  <div class="abs price"><span class="amount">£10</span><span class="pp">PP</span></div>
  <div class="abs includes">
    <div class="label">OFFER INCLUDES :</div>
    <div class="lead">Half An Hour</div>
    <div class="item">TOBOGGAN TRACK</div>
    <div class="lead">Half An Hour</div>
    <div class="item">SLINGSHOT PAINTBALLS</div>
    <div class="note">(20 Paintballs PP)</div>
    <div class="item">SAFE TARGET ARCHERY</div>
    <div class="note">(under Cover And Indoor Ranges)</div>
  </div>

  <div class="abs miss-tag">
    <svg width="260" height="43" viewBox="0 0 260 43"><polygon points="6,0 244,0 260,21.5 244,43 0,43" fill="#ee1c1c"/></svg>
    <span>DON'T MISS IT !</span>
  </div>

  <div class="photo photo-curling" role="img" aria-label="Two people playing mini curling on an indoor wooden lane"></div>
  <div class="abs axe-target" role="img" aria-label="Axe throwing target board"></div>
  <div class="abs ages-panel">
    <div class="big">AGES<br>START<br>FROM<br>4 PLUS</div>
    <div class="rule"></div>
    <div class="sm">ALL ACTIVITIES ARE<br>GREAT FOR<br><span class="gold">CHILDREN AND ADULTS</span></div>
    <div class="xs">SO PERFECT FOR</div>
    <div class="fam">FAMILIES</div>
    <div class="xs">AS WELL AS FRIENDS, PARTIES<br>AND GET TOGETHERS.</div>
  </div>

  <div class="abs cafe-strip"></div>
  <div class="photo photo-cafe" role="img" aria-label="Wood burning stove with two hot chocolates on a table"></div>
  <div class="abs cafe-card">
    <div class="head">CAFÉ OPEN</div>
    <div class="cond">FOR HOT FOOD AND DRINKS</div>
    <div class="ital">In The</div>
    <div class="big">‘FIRESIDE FROST LODGE</div>
    <div class="ital">And The Heated</div>
    <div class="cond" style="margin-top:1px">CHRISTMAS MARQUEE.</div>
  </div>

  <div class="photo photo-gel" role="img" aria-label="Two players aiming bead blasters in a camouflage netted tunnel with coloured lights"></div>

  <svg class="abs wave" viewBox="0 0 960 240" preserveAspectRatio="none" aria-hidden="true">
    <defs><linearGradient id="waveFade" x1="0" y1="0" x2="0" y2="1"><stop offset="0" stop-color="#f7b3b6"/><stop offset="1" stop-color="#ee1c1c"/></linearGradient></defs>
    <path d="M0 60 C120 20 260 40 360 110 C430 160 520 170 640 150 L640 240 L0 240 Z" fill="url(#waveFade)" opacity=".85"/>
    <path d="M0 150 C200 120 420 160 760 200 L960 200 L960 240 L0 240 Z" fill="#f7b3b6" opacity=".7"/>
  </svg>

  <div class="abs also-tag">ALSO AVAILABLE</div>
  <div class="abs addon">
    <div class="head"><small>ADD ON </small>INDOOR ACTIVITIES</div>
    <div class="list">• INCLUDING MINI CURLING &nbsp;• BEAD BLITZ &nbsp;• SAFE AXE THROWING</div>
    <div class="price-line">AIR JUGGLER <span class="y"><small>FROM</small> £3.50<small>PP</small> AND AGE 6 PLUS</span></div>
  </div>

  <div class="abs brand">
    <div class="brand-dot"></div>
    <div class="brand-name">HOLLOWBROOK<br>LEISURE PARK</div>
  </div>

  <div class="abs booking">
    <div class="head">BOOKING IS EASY!</div>
    <div class="sub">DM on this post or email :</div>
  </div>
  <div class="abs email-band">MARTIN@HOLLOWBROOKLEISUREPARK.CO.UK</div>
  <div class="abs avail">for availability of your preferred date and time</div>
  <svg class="abs cursor" viewBox="0 0 32 34" aria-hidden="true"><path d="M3 3 L3 26 L9 20 L14 31 L19 29 L14 18 L23 18 Z" fill="#fff" stroke="#111" stroke-width="2" stroke-linejoin="round"/></svg>
  <div class="abs parking">FREE HUGE CAR PARKS</div>
</main>
</body>
</html>
```